Sales Brochure- Generic Line Card 215mm x 140mm

Design a double-sided brochure similar to the attached sample. Cover Page contains a logo and theme that never changes. However, the background picture and the description text on the lower corner will be changed to advertise multiple services. Reverse-side contains Detailed Descriptive text related to the picture on Cover Page as well as Logo and Contact information for the business. Use the Kelvra Controls website www.kelvracontrols.ca for theme, color and contact information. Also, use attached business card design for theme to match. Use the supplied logo. SIZE 215mm x 140mm

Font styles to use
Sans Serif

Colors

Designer to choose colors to be used in the design.

Requirements
Must have
• Look Similar to Sample Brochure but include Kelvra Controls theme and colors

```html
<!DOCTYPE html>
<html lang="en">
<head>
<meta charset="utf-8">
<title>Kelvra Controls – Pioneering Responsive Machining</title>
<link rel="stylesheet" href="https://fonts.googleapis.com/css2?family=Barlow+Condensed:wght@400;500;600;700;800&display=swap">
<style>
  :root {
    --teal-deep: #083e4b;
    --teal-shadow: #0b4a58;
    --teal-mid: #16707f;
    --teal-steel: #2a94a6;
    --teal-light: #5cc3d3;
    --teal-glint: #8fdbe6;
    --cyan-accent: #17bcd6;
    --cyan-haze: rgba(120, 220, 235, 0.2);
    --band-tint: rgba(6, 60, 74, 0.35);
    --white: #ffffff;
  }
  * { margin: 0; padding: 0; box-sizing: border-box; }
  html, body {
    width: 1200px;
    height: 846px;
    overflow: hidden;
    background: var(--teal-deep);
  }
  .cover {
    position: relative;
    width: 1200px;
    height: 846px;
    overflow: hidden;
    font-family: "Barlow Condensed", "Arial Narrow", sans-serif;
  }
  .cover-photo {
    position: absolute;
    inset: 0;
    background:
      radial-gradient(circle at 17% 28%, var(--teal-glint) 0%, var(--teal-light) 8%, transparent 18%),
      radial-gradient(circle at 75% 30%, var(--teal-glint) 0%, var(--teal-light) 7%, transparent 16%),
      radial-gradient(circle at 46% 84%, var(--teal-light) 0%, transparent 14%),
      radial-gradient(circle at 20% 32%, var(--teal-steel) 0%, var(--teal-steel) 30%, #1f8294 35%, transparent 37%),
      radial-gradient(circle at 78% 31%, var(--teal-steel) 0%, var(--teal-steel) 26%, #1f8294 31%, transparent 33%),
      radial-gradient(circle at 46% 86%, var(--teal-steel) 0%, var(--teal-steel) 22%, #1f8294 27%, transparent 29%),
      radial-gradient(circle at 10% 100%, #2a8e9f 0%, transparent 20%),
      radial-gradient(ellipse at 47% 42%, var(--teal-deep) 0%, var(--teal-shadow) 20%, transparent 40%),
      linear-gradient(160deg, var(--teal-mid) 0%, var(--teal-shadow) 100%);
  }
  .top-band {
    position: absolute;
    left: 0; top: 0;
    width: 1200px;
    height: 199px;
    background: var(--band-tint);
  }
  .brand {
    position: absolute;
    left: 50px;
    top: 78px;
    display: flex;
    align-items: center;
    gap: 16px;
    color: var(--white);
  }
  .brand-mark {
    width: 70px;
    height: 70px;
    background: var(--white);
  }
  .brand-name {
    font-size: 66px;
    font-weight: 800;
    line-height: 1;
    text-transform: uppercase;
    letter-spacing: 0.01em;
  }
  .service-haze {
    position: absolute;
    left: 583px;
    top: 611px;
    width: 617px;
    height: 235px;
    background: var(--cyan-haze);
    border-top-left-radius: 120px;
  }
  .service-tag {
    position: absolute;
    left: 598px;
    top: 627px;
    width: 602px;
    height: 219px;
    background: var(--cyan-accent);
    border-top-left-radius: 112px;
    border-bottom-left-radius: 112px;
    padding: 14px 52px 0 0;
    text-align: right;
    color: var(--white);
  }
  .service-line {
    display: block;
    font-size: 66px;
    line-height: 65px;
    letter-spacing: 0.17em;
    margin-right: -0.17em;
    text-transform: uppercase;
  }
  .service-line--light { font-weight: 500; }
  .service-line--bold { font-weight: 700; }
</style>
</head>
<body>
  <main class="cover">
    <div class="cover-photo" role="img" aria-label="Close-up photograph of three large interlocking steel gears, tinted teal"></div>
    <div class="top-band"></div>

    <div class="brand">
      <span class="brand-mark"></span>
      <span class="brand-name">Kelvra Controls</span>
    </div>

    <div class="service-haze"></div>
    <section class="service-tag">
      <span class="service-line service-line--light">Pioneering</span>
      <span class="service-line service-line--bold">Responsive</span>
      <span class="service-line service-line--light">Machining</span>
    </section>
  </main>
</body>
</html>
```